Letterhead Design Project

Looking for letterhead designs for Brastova Mining.

I am looking for a letterhead design in conjunction with a business card design. I have opened contests for both but ask that if you submit a letterhead design you also submit a business card design with a corresponding look/feel.

Brastova Mining is a B2B company that buys and sells large machinery tires within the coal mining industry. The design should the strong, crisp and masculine. I have uploaded the company logo and mock-up of the back of the company's business card.

Color scheme should be grey/green/black

Contact information to include:
Name: Dale Whitford
Title: Managing Director
Phone: 555-231-4097
Address: 1817 Pellam #3 Dallas, TX 75290
Email: Dale@Brastova.example
Updates

Project Deadline Extended
Reason: Looking for a more refined, elegant letterhead than what's been submitted as of yet. Here is a sample of what we're looking for: http://www.plumcrestgallery.example/letterhead-designs/ We will also be increasing the payment.

Industry/Entity Type

Coal Mining

```html
<!DOCTYPE html>
<html lang="en">
<head>
<meta charset="utf-8">
<title>Brastova Mining – Letterhead</title>
<link rel="stylesheet" href="https://fonts.googleapis.com/css2?family=Montserrat:wght@400;600;700&display=swap">
<style>
  :root {
    --backdrop: #8f8f8f;
    --paper: #ffffff;
    --ink: #3a3a3a;
    --ink-soft: #555555;
    --green: #6cb52d;
    --green-soft: #9fd16f;
  }
  html, body {
    margin: 0;
    padding: 0;
    width: 1200px;
    height: 896px;
    overflow: hidden;
    background: var(--backdrop);
    font-family: "Montserrat", Arial, sans-serif;
  }
  .letterhead {
    position: absolute;
    left: 301px;
    top: 24px;
    width: 598px;
    height: 848px;
    background: var(--paper);
    box-shadow: 0 6px 22px rgba(0,0,0,0.28);
    overflow: hidden;
  }
  .accent-band {
    position: absolute;
    right: 0;
    background: linear-gradient(90deg, var(--green-soft), var(--green));
  }
  .accent-band--top {
    top: 0;
    width: 118px;
    height: 16px;
  }
  .accent-band--bottom {
    bottom: 0;
    width: 230px;
    height: 34px;
  }
  .masthead {
    position: absolute;
    top: 40px;
    right: 34px;
  }
  .brand {
    display: flex;
    align-items: center;
    gap: 8px;
  }
  .brand__mark {
    width: 20px;
    height: 20px;
    background: var(--green);
  }
  .brand__name {
    font-weight: 700;
    font-size: 22px;
    letter-spacing: 2px;
    color: var(--ink);
    text-transform: uppercase;
    line-height: 1;
  }
  .contact {
    margin: 8px 0 0 28px;
    font-size: 9.5px;
    color: var(--ink-soft);
    line-height: 1.55;
  }
  .contact__person {
    font-weight: 600;
    color: var(--ink);
  }
  .contact__label {
    color: var(--green);
    font-weight: 600;
  }
</style>
</head>
<body>
  <main class="letterhead">
    <div class="accent-band accent-band--top" role="img" aria-label="Green diagonal stripe band"></div>

    <header class="masthead">
      <div class="brand">
        <span class="brand__mark"></span>
        <span class="brand__name">Brastova Mining</span>
      </div>
      <div class="contact">
        <div class="contact__person">Dale Whitford, Managing Director</div>
        <div class="contact__address">1817 Pellam #3 Dallas, TX 75290</div>
        <div class="contact__lines">
          <span class="contact__label">E:</span> Dale@Brastova.example
          &nbsp;<span class="contact__label">Ph:</span> 555-231-4097
        </div>
      </div>
    </header>

    <div class="accent-band accent-band--bottom" role="img" aria-label="Green diagonal stripe band"></div>
  </main>
</body>
</html>
```